"Da'wah Workshop" - Islamic Flyer

Hi,

The details needed on the flyer are below.

Also, some example ideas for the design are attached. Feel free to create any design you like.

_________________

Free Event!

OKTEL and BROVT presents:
(OKTEL and BROVT Logo)

Da'wah Workshop

Speakers:
Br. Karim Fadel
(OLBU)

Br. Tariq Mansour
(TOVNE)

Sunday 17th May
1:00pm - 5:00pm

Venue:
Lanterns Cafe
Level 6 Quarry House
Bellcrest College

For more info, call 0488 752 204

[Facebook Logo] OKTEL

```html
<!DOCTYPE html>
<html lang="en">
<head>
<meta charset="utf-8">
<title>Da'wah Workshop Flyer</title>
<link rel="stylesheet" href="https://fonts.googleapis.com/css2?family=Cinzel:wght@700&family=Lato:wght@700;900&family=Montserrat:wght@700&family=Playfair+Display:ital@1&display=swap">
<style>
  :root {
    --teal: #7ccbd1;
    --navy: #1c2b5e;
    --tan: #b08d58;
    --orange: #e98f38;
    --cream: #f3ece1;
    --panel: rgba(246, 240, 230, 0.6);
    --stone-light: #ecdcc2;
    --stone-mid: #d2b894;
    --stone-dark: #b89a72;
    --page-bg: #e9e8ec;
    --white: #ffffff;
  }
  * { margin: 0; padding: 0; box-sizing: border-box; }
  html, body { width: 1040px; height: 1200px; overflow: hidden; }
  body { background: var(--page-bg); position: relative; font-family: "Lato", sans-serif; }

  .flyer { position: absolute; left: 110px; top: 47px; width: 820px; height: 1105px; background: var(--tan); box-shadow: 0 8px 24px rgba(0,0,0,0.18); overflow: hidden; }

  .header { position: absolute; left: 0; top: 0; width: 820px; height: 248px; background: var(--teal); }
  .title { position: absolute; top: 44px; width: 100%; text-align: center; font-family: "Cinzel", serif; font-weight: 700; font-size: 56px; color: var(--navy); letter-spacing: 1px; }
  .free-badge { position: absolute; left: 285px; top: 130px; width: 262px; height: 37px; background: var(--tan); border: 1px solid var(--cream); text-align: center; line-height: 35px; font-family: "Playfair Display", serif; font-style: italic; font-size: 23px; color: var(--cream); }
  .presented { position: absolute; left: 230px; top: 202px; font-family: "Montserrat", sans-serif; font-weight: 700; font-size: 19px; color: var(--orange); letter-spacing: 0.5px; }
  .partners { position: absolute; left: 424px; top: 192px; width: 162px; height: 44px; background: var(--white); display: flex; }
  .partners span { flex: 1; display: flex; align-items: center; justify-content: center; font-family: "Lato", sans-serif; font-weight: 900; font-size: 16px; color: var(--white); }
  .partners .host { background: var(--navy); }
  .partners .co-host { color: var(--navy); }

  .rule { position: absolute; left: 0; top: 248px; width: 820px; height: 11px; background: var(--navy); }
  .schedule { position: absolute; left: 0; top: 259px; width: 820px; height: 63px; display: flex; align-items: center; justify-content: center; gap: 48px; font-family: "Lato", sans-serif; font-weight: 700; font-variant: small-caps; font-size: 32px; color: var(--navy); }
  .schedule .divider { font-weight: 400; }

  .hero { position: absolute; left: 0; top: 322px; width: 820px; height: 705px; background: linear-gradient(160deg, var(--stone-light) 0%, var(--stone-mid) 55%, var(--stone-dark) 100%); }

  .info-panel { position: absolute; left: 412px; top: 600px; width: 408px; height: 412px; background: var(--panel); }
  .tab { position: absolute; left: 412px; width: 408px; }
  .tab svg { position: absolute; left: 0; top: 0; }
  .tab-label { position: absolute; left: 36px; top: 0; font-family: "Montserrat", sans-serif; font-weight: 700; color: var(--orange); }
  .tab-speakers { top: 544px; height: 56px; }
  .tab-speakers .tab-label { font-size: 32px; line-height: 56px; }
  .tab-venue { top: 795px; height: 53px; }
  .tab-venue .tab-label { font-size: 30px; line-height: 53px; }

  .name, .affil, .venue-line { position: absolute; left: 449px; color: var(--navy); }
  .name, .venue-line { font-family: "Lato", sans-serif; font-weight: 900; font-variant: small-caps; font-size: 29px; }
  .affil { font-family: "Lato", sans-serif; font-weight: 700; font-size: 20px; }

  .footer { position: absolute; left: 0; top: 1027px; width: 820px; height: 78px; background: var(--tan); }
  .more-info { position: absolute; left: 52px; top: 20px; display: flex; align-items: center; gap: 10px; font-family: "Lato", sans-serif; font-weight: 900; font-variant: small-caps; font-size: 28px; color: var(--white); }
  .more-info .phone { color: var(--orange); font-size: 29px; font-variant: normal; }
  .social { position: absolute; left: 564px; top: 11px; width: 208px; height: 55px; background: var(--teal); display: flex; align-items: center; }
  .social .mark { width: 55px; height: 55px; background: var(--navy); }
  .social .handle { flex: 1; text-align: center; font-family: "Lato", sans-serif; font-weight: 900; font-size: 26px; color: var(--white); }
</style>
</head>
<body>
  <main class="flyer">
    <header class="header">
      <h1 class="title">Da'wah Workshop</h1>
      <div class="free-badge">Free ISLAMIC Event!</div>
      <div class="presented">PRESENTED BY</div>
      <div class="partners"><span class="host">OKTEL</span><span class="co-host">BROVT</span></div>
    </header>
    <div class="rule"></div>
    <div class="schedule"><span>Sunday 17th May</span><span class="divider">|</span><span>1:00pm – 5:00pm</span></div>

    <div class="hero" role="img" aria-label="Photograph of a carved stone Moorish archway framing a blue mosaic tile doorway"></div>

    <div class="info-panel"></div>

    <div class="tab tab-speakers">
      <svg width="408" height="56" viewBox="0 0 408 56">
        <rect x="0" y="0" width="250" height="56" fill="var(--cream)" opacity="0.9"/>
        <polygon points="250,0 330,0 370,56 290,56" fill="var(--tan)"/>
        <polygon points="330,0 408,0 408,56 370,56" fill="var(--teal)"/>
      </svg>
      <div class="tab-label">SPEAKERS:</div>
    </div>

    <div class="name" style="top:612px">Br. Karim Fadel</div>
    <div class="affil" style="top:657px">(OLBU)</div>
    <div class="name" style="top:698px">Br. Tariq Mansour</div>
    <div class="affil" style="top:742px">(TOVNE)</div>

    <div class="tab tab-venue">
      <svg width="408" height="53" viewBox="0 0 408 53">
        <rect x="0" y="0" width="250" height="53" fill="var(--cream)" opacity="0.9"/>
        <polygon points="250,0 330,0 370,53 290,53" fill="var(--tan)"/>
        <polygon points="330,0 408,0 408,53 370,53" fill="var(--teal)"/>
      </svg>
      <div class="tab-label">VENUE :</div>
    </div>

    <div class="venue-line" style="top:864px">Lanterns Cafe</div>
    <div class="venue-line" style="top:904px">Level 6 Quarry House</div>
    <div class="venue-line" style="top:944px">Bellcrest College</div>

    <footer class="footer">
      <div class="more-info">
        <span>For more info</span>
        <svg width="26" height="28" viewBox="0 0 24 24" aria-hidden="true"><path fill="var(--teal)" d="M6.6 10.8a15.1 15.1 0 0 0 6.6 6.6l2.2-2.2a1 1 0 0 1 1-.25 11.4 11.4 0 0 0 3.6.57 1 1 0 0 1 1 1V20a1 1 0 0 1-1 1A17 17 0 0 1 3 4a1 1 0 0 1 1-1h3.5a1 1 0 0 1 1 1c0 1.25.2 2.45.57 3.57a1 1 0 0 1-.25 1z"/></svg>
        <span class="phone">0488 752 204</span>
      </div>
      <div class="social"><div class="mark"></div><div class="handle">OKTEL</div></div>
    </footer>
  </main>
</body>
</html>
```